Reggie Vosburn - Free Personalised Health Consultation - "Every body walks its own path"

This flyer will be left on tables/seats at speaking events and seminars and used to attain leads.

Top half will have "SMS me for a FREE Personalised Health Consultation" and my picture (see www.reggievosburn.example and pick most engaging photo) and underneath my contact details. It must have lines with "Notes:" halfway down so people can take notes at the seminar and lines on the back with my contact details again and "Notes: with lines.

I am having a business card also being designed by Plotnest for same and would like the flyer and business card to carry a similar feel/look for consistency.

Below is the brief for the business card being designed:
Business Card for www.reggievosburn.example site. It is a trust site and I use it for 1:1 relatable connections. It is the one I use for building intimate 1:1 trust building and Exec Coaching Services and programs for high wealth individuals and corporates. I also have a commercial programmatic site of my personal health products and services and programs for main stream one to many. www.crossgenvitality.example that can also provoke thought for the www.reggievosburn.example business card. (mind you will get a separate business card for that site, but want to provide context). It has a logo which you may want to draw from in designing the reggievosburn business card which is personal and is about building my brand. There is also a reggievosburn personal KX page and reggievosburn business KX page. I am a Certified Talent Compass 4.1 Coach with Verrick and you can get a corporate brief of me on there to give you more context https://www.verricktalenthub.example/coach/en-us/directory?search=reggie

Target Market(s)

Exec, IT, Health conscious. Corporates wanting to run Health and Wellness programs. Those wanting to go from good to great. Millennials to Middleaged.

Industry/Entity Type

Health And Wellness

Font styles to use
Sans Serif
Other font styles liked:
• Arial and Calibri ok too

Colors

Designer to choose colors to be used in the design.

Requirements
Must have
• Picture of me - use best from www.reggievosburn.example or can send one you choose.
• Contact details like my buisness card being designed by you guys in separate project.
• Name: Reggie Vosburn
• email: reggie@reggievosburn.,example
• Phone: Australia +61 455 318 026 Singapore: +65 8342 1960
Nice to have
• Open to ideas

```html
<!DOCTYPE html>
<html lang="en">
<head>
<meta charset="utf-8">
<title>Reggie Vosburn – Free Personalised Health Consultation</title>
<link href="https://fonts.googleapis.com/css2?family=Roboto+Condensed:wght@300;400;500;700&family=Open+Sans:wght@400&display=swap" rel="stylesheet">
<style>
  :root {
    --page-bg: #e6e6e6;
    --paper: #ffffff;
    --ink: #0b0b0b;
    --panel-dark: #121212;
    --panel-mid: #222222;
    --photo-light: #f2f2f2;
    --photo-dark: #2a2a2a;
    --text-light: #ffffff;
    --bar: rgba(185,185,185,0.92);
  }
  * { margin: 0; padding: 0; box-sizing: border-box; }
  html, body { width: 1200px; height: 1200px; overflow: hidden; background: var(--page-bg); }
  .flyer {
    position: absolute; left: 224px; top: 72px;
    width: 753px; height: 1056px;
    background: var(--paper); overflow: hidden;
    font-family: "Roboto Condensed", Arial, sans-serif;
  }
  .portrait {
    position: absolute; left: 0; top: 272px; width: 356px; height: 784px;
    background: linear-gradient(180deg, var(--photo-light) 0%, #b5b5b5 30%, #555 55%, var(--photo-dark) 75%, #151515 100%);
  }
  .dark-panel {
    position: absolute; left: 356px; top: 0; width: 397px; height: 1056px;
    background: radial-gradient(ellipse at 40% 35%, var(--panel-mid) 0%, var(--panel-dark) 60%, #080808 100%);
  }
  .headline {
    position: absolute; left: 26px; top: 16px; width: 730px; white-space: nowrap;
  }
  .headline--on-light { color: var(--ink); clip-path: inset(0 400px 0 0); }
  .headline--on-dark { color: var(--text-light); clip-path: inset(0 0 0 330px); }
  .headline__lead { display: block; font-weight: 300; font-size: 56px; line-height: 62px; letter-spacing: -0.5px; }
  .headline__main { display: block; font-weight: 700; font-size: 72px; line-height: 88px; letter-spacing: -0.5px; margin-top: 4px; }
  .bio__name {
    position: absolute; left: 409px; top: 340px; width: 278px;
    color: var(--text-light); text-align: center;
    font-weight: 400; font-size: 36px; line-height: 40px;
    padding-bottom: 2px; border-bottom: 3px solid var(--text-light);
  }
  .bio__text {
    position: absolute; left: 384px; top: 407px; width: 345px;
    color: var(--text-light);
    font-family: "Open Sans", Calibri, Arial, sans-serif;
    font-size: 10.6px; line-height: 16.2px; text-align: justify;
  }
  .bio__text p + p { margin-top: 16.2px; }
  .divider {
    position: absolute; left: 405px; top: 862px; width: 302px; height: 2px;
    background: linear-gradient(90deg, transparent, var(--text-light) 12%, var(--text-light) 88%, transparent);
  }
  .phones {
    position: absolute; left: 433px; top: 896px; color: var(--text-light);
    font-weight: 500; font-size: 21px; line-height: 26px;
  }
  .contact-bar {
    position: absolute; left: 0; top: 968px; width: 753px; height: 44px;
    display: flex; background: var(--bar); color: var(--ink); font-size: 19px; font-weight: 400;
  }
  .contact-bar__web { width: 356px; display: flex; align-items: center; justify-content: center; }
  .contact-bar__mail { flex: 1; display: flex; align-items: center; padding-left: 30px; gap: 12px; }
</style>
</head>
<body>
  <main class="flyer">
    <div class="portrait" role="img" aria-label="Black and white portrait of Reggie Vosburn smiling with arms crossed, wearing a dark V-neck t-shirt"></div>
    <div class="dark-panel" role="img" aria-label="Dark, faded background photo of a celebrating person"></div>

    <h1 class="headline headline--on-light">
      <span class="headline__lead">SMS ME FOR A FREE</span>
      <span class="headline__main">PERSONALISED HEALTH<br>CONSULTATION</span>
    </h1>
    <div class="headline headline--on-dark" aria-hidden="true">
      <span class="headline__lead">SMS ME FOR A FREE</span>
      <span class="headline__main">PERSONALISED HEALTH<br>CONSULTATION</span>
    </div>

    <h2 class="bio__name">REGGIE VOSBURN</h2>
    <div class="bio__text">
      <p>Reggie Vosburn (aka ReggieV) describes himself as a “Middleaged Millennial”. In probing further I discover that this is all about his uplifting and inspiring perspective on life. A habitual attitude reinforced by a healthy self made mindset. He refers quite often to the 2.0 (some “IT” lingo) chapter of one’s life as they hit Middleage and how he can guide their transformation to regain their youthful vitality leading, healthier, easier, more lucrative, long and fun second half by leveraging strengths they already have.</p>
      <p>His corporate adventure of 30 years spans 1.5 million km on 147 trips through 23 countries and 99 cities, helping many of the adored traditional IT corporates and in the latter parts of his career, more fun and young “born in the cloud” startup companies scale their businesses through building and developing their business partner networks so they could scale their market reach to many more customers.</p>
      <p>He became what the industry began to class as a “Unicorn” in his industry due to his broad and diverse experience from large corporate IT, like Corvane and Helixon, to startups through the tech boom and crash years and then being a visionary pioneer of SaaS (Software as a Service ie the move to the “Cloud” before the term “Cloud” was even coined) back in 2007 with his own SaaS distribution business startup (great idea, but a bit early with not enough $$$ as is often the case).</p>
    </div>

    <div class="divider"></div>

    <div class="phones">
      <div>AUSTRALIA +61 455 318 026</div>
      <div>SINGAPORE: +65 8342 1960</div>
    </div>

    <footer class="contact-bar">
      <div class="contact-bar__web">WWW.REGGIEVOSBURN.EXAMPLE</div>
      <div class="contact-bar__mail">
        <svg width="36" height="20" viewBox="0 0 36 20" aria-hidden="true">
          <rect x="1" y="1" width="34" height="18" fill="none" stroke="#0b0b0b" stroke-width="2"/>
          <polyline points="1,1 18,12 35,1" fill="none" stroke="#0b0b0b" stroke-width="2"/>
        </svg>
        <span>REGGIE@REGGIEVOSBURN.EXAMPLE</span>
      </div>
    </footer>
  </main>
</body>
</html>
```